Tavrel Fitness business cards

I need a business card for my company called Tavrel Fitness. I am a certified personal trainer, QMB certified, Hippo Pilates certified, and Vital paths certified. I am also an independent KORVEL rep, the number #1 rated nutritional and supplement product in the country. The card needs to convey Health, Wellness, Living Life and Loving It. I want it to be clean, sharp, eye-catching. Tantalizing.
Updates

for some reason, I'm unable to upload the pics I need. Stay tuned..

Industry/Entity Type

Business

Contact Information for Business Card

Tavrel Fitness
Mona Lykkestad, Owner
mona@tavrelfitness-example.com
555-203-4471
tavrelfitness-example.com
mona@tavrelfitness-example.com

Font styles to use
Serif

Requirements
Must have
• Must use pic of me and KORVEL logo

```html
<!DOCTYPE html>
<html lang="en">
<head>
<meta charset="utf-8">
<title>Tavrel Fitness – Business Card</title>
<link rel="stylesheet" href="https://fonts.googleapis.com/css2?family=Lobster&display=swap">
<style>
  :root {
    --card-bg: #e4e8e7;
    --band-white: #ffffff;
    --brand-blue: #1446d8;
    --accent-blue: #6d8ae2;
    --ink: #3b3b3b;
    --mint: #aef5e2;
    --partner-tint: #d3dbe7;
    --photo-light: #f0e2c8;
    --photo-mid: #d9a47c;
    --photo-dark: #9a6a4c;
  }
  * { margin: 0; padding: 0; box-sizing: border-box; }
  html, body {
    width: 1200px; height: 702px; overflow: hidden;
    background: var(--card-bg);
  }
  .card {
    position: relative; width: 1200px; height: 702px;
    background: var(--card-bg);
    font-family: "Lobster", cursive;
    overflow: hidden;
  }
  .card__stripes { position: absolute; inset: 0; }
  .title-band {
    position: absolute; left: 48px; top: 61px; width: 1102px; height: 77px;
    background: var(--band-white);
    display: flex; align-items: center; justify-content: center;
  }
  .title-band__name {
    color: var(--brand-blue); font-size: 68px; line-height: 1;
    font-weight: 400; padding-top: 4px;
  }
  .contact {
    position: absolute; right: 58px; top: 142px; text-align: right;
    color: var(--ink); font-size: 37px; line-height: 51px;
  }
  .partner {
    position: absolute; left: 730px; top: 352px; width: 380px; height: 300px;
    display: flex; flex-direction: column; align-items: center;
  }
  .partner__dot {
    width: 200px; height: 200px; border-radius: 50%;
    background: var(--partner-tint); opacity: 0.55;
  }
  .partner__name {
    margin-top: 18px; color: var(--partner-tint); font-size: 64px; line-height: 1;
    letter-spacing: 6px;
  }
  .portrait {
    position: absolute; left: 0; top: 182px; width: 235px; height: 520px;
    background: linear-gradient(180deg, var(--photo-light) 0%, var(--photo-mid) 45%, var(--photo-dark) 100%);
    -webkit-mask-image: linear-gradient(90deg, #000 75%, transparent 100%);
    mask-image: linear-gradient(90deg, #000 75%, transparent 100%);
  }
  .keyword {
    position: absolute; color: var(--accent-blue); font-size: 22px; line-height: 1;
  }
  .keyword--wellness { left: 476px; top: 252px; }
  .keyword--health { left: 248px; top: 366px; }
  .keyword--exercise { left: 379px; top: 488px; }
  .tagline {
    position: absolute; left: 116px; top: 428px;
    color: var(--brand-blue); font-size: 44px; line-height: 1;
  }
</style>
</head>
<body>
<main class="card">
  <svg class="card__stripes" width="1200" height="702" viewBox="0 0 1200 702" aria-hidden="true">
    <polygon points="487,271 597,271 155,702 100,702" fill="var(--mint)"/>
    <polygon points="332,393 371,393 254,520 216,520" fill="var(--mint)"/>
  </svg>

  <header class="title-band">
    <h1 class="title-band__name">Tavrel Fitness</h1>
  </header>

  <address class="contact" style="font-style:normal">
    <div class="contact__name">Mona Lykkestad</div>
    <div class="contact__phone">Owner 555-203-4471</div>
    <div class="contact__web">tavrelfitness-example.com</div>
    <div class="contact__email">mona@tavrelfitness-example.com</div>
  </address>

  <div class="partner">
    <div class="partner__dot"></div>
    <div class="partner__name">KORVEL</div>
  </div>

  <div class="portrait" role="img" aria-label="Photo of the trainer, a blonde woman in sportswear leaning toward the camera"></div>

  <span class="keyword keyword--wellness">WELLNESS</span>
  <span class="keyword keyword--health">HEALTH</span>
  <p class="tagline">Living Life and Loving It</p>
  <span class="keyword keyword--exercise">EXERCISE</span>
</main>
</body>
</html>
```